BrightLoom business card

We are a performing arts company providing training (to both kids and adults) as well as performers for events. We hope to bring joy and confidence on stage to the people we train, as well as joy to the audience when our artistes perform. Designs should convey the joy, confidence and vibrancy on stage. Design business card using the attached logo. Card to include name, mobile tel, email address, company address, and website. Double sided. To also include the following list of what the company does:
• Training & Enrichment
• Private & Corporate Entertainment
- Music composition & production

Industry/Entity Type

Training

Contact Information for Business Card

Card to include name, mobile tel, email address, company address, and website. Double sided. To also include the following list of what the company does:
• Training & Enrichment

Requirements
Nice to have
• Card need not be the traditional rectangular in shape but not too outrageous.

```html
<!DOCTYPE html>
<html lang="en">
<head>
<meta charset="utf-8">
<title>BrightLoom Business Card</title>
<link href="https://fonts.googleapis.com/css2?family=Mako&display=swap" rel="stylesheet">
<style>
  :root {
    --page-bg: #e4e4e2;
    --card-white: #ffffff;
    --brand-green: #5a9a3a;
    --green-light: #7dc242;
    --green-dark: #3a8a3a;
    --panel-grey-a: #86837f;
    --panel-grey-b: #a19d9a;
    --ink: #1c1c1c;
    --brand-navy: #23236e;
  }
  * { margin: 0; padding: 0; box-sizing: border-box; }
  html, body {
    width: 1200px; height: 902px; overflow: hidden;
    background: var(--page-bg);
    font-family: "Mako", sans-serif;
  }
  .card {
    position: absolute; left: 80px; top: 153px;
    width: 1040px; height: 595px;
    box-shadow: 0 10px 30px rgba(0,0,0,0.18);
    overflow: hidden;
  }
  .card-shapes { position: absolute; inset: 0; }
  .contact { position: absolute; left: 68px; top: 0; color: var(--ink); }
  .name {
    position: absolute; top: 98px; left: 0; white-space: nowrap;
    font-size: 35px; color: var(--brand-green); font-weight: 400;
  }
  .title { position: absolute; top: 137px; left: 2px; font-size: 27px; white-space: nowrap; }
  .address { position: absolute; top: 210px; left: 2px; font-size: 24px; line-height: 31px; white-space: nowrap; }
  .channels { position: absolute; top: 300px; left: 8px; list-style: none; font-size: 24px; line-height: 30px; }
  .channels li { display: flex; align-items: center; gap: 14px; white-space: nowrap; }
  .channels svg { width: 20px; height: 20px; flex: none; }
  .services { position: absolute; top: 416px; left: 0; list-style: none; font-size: 24px; line-height: 30.5px; white-space: nowrap; }
  .brand {
    position: absolute; left: 640px; width: 400px; top: 165px;
    display: flex; flex-direction: column; align-items: center; gap: 22px;
  }
  .brand-dot { width: 86px; height: 86px; border-radius: 50%; background: var(--brand-navy); }
  .brand-name { font-size: 62px; color: var(--brand-navy); font-weight: 400; letter-spacing: 1px; }
</style>
</head>
<body>
<div class="card">
  <svg class="card-shapes" viewBox="0 0 1040 595" width="1040" height="595">
    <defs>
      <linearGradient id="panelGrey" x1="0" y1="0" x2="1" y2="1">
        <stop offset="0" stop-color="var(--panel-grey-a)"/>
        <stop offset="1" stop-color="var(--panel-grey-b)"/>
      </linearGradient>
      <linearGradient id="accentGreen" x1="0" y1="0" x2="0" y2="1">
        <stop offset="0" stop-color="var(--green-light)"/>
        <stop offset="1" stop-color="var(--green-dark)"/>
      </linearGradient>
    </defs>
    <rect width="1040" height="595" fill="url(#panelGrey)"/>
    <polygon points="0,0 480,0 636,595 0,595" fill="url(#accentGreen)"/>
    <polygon points="0,0 418,0 628,595 0,595" fill="var(--card-white)"/>
  </svg>

  <div class="contact">
    <h1 class="name">Employee Name</h1>
    <p class="title">Your Title</p>
    <p class="address">Your Adress Inc 2nd Lane<br>Ave Edison, NJ 00000</p>
    <ul class="channels">
      <li>
        <svg viewBox="0 0 20 20" aria-hidden="true"><rect width="20" height="20" rx="2" fill="var(--brand-green)"/><rect x="6" y="4" width="8" height="12" rx="1" fill="none" stroke="#fff" stroke-width="1.6"/></svg>
        0012 3456 789
      </li>
      <li>
        <svg viewBox="0 0 20 20" aria-hidden="true"><rect width="20" height="20" rx="2" fill="var(--brand-green)"/><rect x="4" y="6" width="12" height="8" fill="none" stroke="#fff" stroke-width="1.5"/><polyline points="4,6 10,11 16,6" fill="none" stroke="#fff" stroke-width="1.5"/></svg>
        info@youremail.com
      </li>
      <li>
        <svg viewBox="0 0 20 20" aria-hidden="true"><rect width="20" height="20" rx="2" fill="var(--brand-green)"/><circle cx="10" cy="10" r="6" fill="none" stroke="#fff" stroke-width="1.5"/><path d="M4 10h12M10 4c-3 3-3 9 0 12M10 4c3 3 3 9 0 12" fill="none" stroke="#fff" stroke-width="1.2"/></svg>
        www.yourwebsite.com
      </li>
    </ul>
    <ul class="services">
      <li>Training &amp; Enrichment</li>
      <li>Private &amp; Corporate Entertainment</li>
      <li>Music composition &amp; production</li>
    </ul>
  </div>

  <div class="brand">
    <div class="brand-dot"></div>
    <p class="brand-name">BrightLoom</p>
  </div>
</div>
</body>
</html>
```